Oil and Gas Letterhead Design Tweak

Simple letterhead information and design tweak.

Please note, we don't want to change the design or logo of the letterhead only the small changes mentioned below.

We need to change the company name up top to "Northvale Petrotek FZCO"

Also, we need to include in the footer the following information. I have attached an image of roughly how we would like to have it displayed in the footer.

Footer Details:

Northvale Petrotek FZCO,
Unit No. 2378, FZCO Trade Hub, level No. 1, K&P 7, Dubai, United Arab Emirates
Northvale Petrotek FZCO is registered as a free zone company under the rules & regulations of FZCO

Target Market(s)

O&G Market

Industry/Entity Type

Oil And Gas

Font styles to use
Sans Serif

Colors

Designer to choose colors to be used in the design.

Requirements
Must have
• Change the company name to Northvale Petrotek FZCO
• Include the footer on the bottom of the first and continuation page
Should not have
• Should not change the design or logo of the letterhead, only the specified changes mentioned above

```html
<!DOCTYPE html>
<html lang="en">
<head>
<meta charset="utf-8">
<title>Northvale Petrotek FZCO — Letterhead</title>
<link href="https://fonts.googleapis.com/css2?family=Montserrat:wght@400;500&family=Source+Sans+3:wght@400&family=Arimo:wght@700&display=swap" rel="stylesheet">
<style>
  :root {
    --backdrop: #ececec;
    --paper: #ffffff;
    --brand-blue: #0f56a5;
    --brand-red: #e3202a;
    --ink-navy: #1b2a63;
    --ink-body: #454545;
    --ink-heading: #1a1a1a;
    --sig-tone: #e4e4e4;
  }
  * { box-sizing: border-box; margin: 0; padding: 0; }
  html, body { width: 1200px; height: 1200px; overflow: hidden; }
  body { background: var(--backdrop); position: relative; }

  .letterhead {
    position: absolute; left: 189px; top: 20px;
    width: 822px; height: 1160px;
    background: var(--paper);
    box-shadow: 0 4px 18px rgba(0,0,0,0.12);
    overflow: hidden;
  }

  .top-bar { position: absolute; top: 0; height: 14px; }
  .top-bar--blue { left: 0; width: 188px; background: var(--brand-blue); clip-path: polygon(0 0, 100% 0, 96.5% 100%, 0 100%); }
  .top-bar--red { left: 256px; right: 0; background: var(--brand-red); clip-path: polygon(0 0, 100% 0, 100% 100%, 5px 100%); }

  .masthead {
    position: absolute; left: 206px; top: 44px;
    display: flex; align-items: center; gap: 18px;
  }
  .masthead__mark { width: 26px; height: 26px; background: var(--brand-red); }
  .masthead__name {
    font-family: "Montserrat", sans-serif; font-weight: 400;
    font-size: 24px; letter-spacing: 0.6px; color: var(--ink-heading);
    text-transform: uppercase;
  }

  .letter { position: absolute; left: 63px; top: 279px; width: 696px; }
  .letter__greeting {
    font-family: "Arimo", sans-serif; font-weight: 700;
    font-size: 18px; color: var(--ink-navy); margin-bottom: 24px;
  }
  .letter__para {
    font-family: "Source Sans 3", sans-serif; font-size: 16.6px;
    line-height: 21.6px; color: var(--ink-body);
    text-align: justify; margin-bottom: 21.5px;
  }
  .letter__signature {
    width: 154px; height: 72px; margin-top: 6px;
    background: linear-gradient(90deg, var(--sig-tone), #f3f3f3);
    border-radius: 4px;
  }

  .footer-band {
    position: absolute; left: 0; right: 0; bottom: 0; height: 54px;
  }
  .footer-band__mark {
    position: absolute; left: 76px; top: 14px;
    width: 24px; height: 24px; border-radius: 50%; background: var(--brand-red);
  }
  .footer-band__panel {
    position: absolute; left: 110px; right: 0; top: 0; bottom: 0;
    background: var(--brand-blue); color: #fff;
    font-family: "Montserrat", sans-serif; font-weight: 400;
    padding: 3px 0 0 11px;
  }
  .footer-band__name { font-size: 12.5px; text-transform: uppercase; line-height: 17px; }
  .footer-band__line { font-size: 11.4px; line-height: 15px; }
</style>
</head>
<body>
  <main class="letterhead">
    <div class="top-bar top-bar--blue"></div>
    <div class="top-bar top-bar--red"></div>

    <header class="masthead">
      <span class="masthead__mark"></span>
      <span class="masthead__name">Northvale Petrotek FZCO</span>
    </header>

    <section class="letter">
      <p class="letter__greeting">Dear Mr. Adrian,</p>
      <p class="letter__para">Lorem Ipsum is simply dummy text of the printing and typesetting industry. Lorem Ipsum has been the industry's standard dummy text ever since the 1500s, when an unknown printer took a galley of type and scrambled it to make a type specimen book. It has survived not only five centuries, but also the leap into electronic typesetting, remaining essentially unchanged.</p>
      <p class="letter__para">The standard chunk of Lorem Ipsum used since the 1500s is reproduced below for those interested. Sections 1.10.32 and 1.10.33 from "de Finibus Bonorum et Malorum" by Verano are also reproduced in their exact original form, accompanied by English versions from the 1914 translation by L. Marlowe</p>
      <p class="letter__para">Lorem Ipsum is simply dummy text of the printing and typesetting industry. Lorem Ipsum has been the industry's standard dummy text ever since the 1500s, when an unknown printer took a galley of type and scrambled it to make a type specimen book. It has survived not only five centuries, but also the leap into electronic typesetting, remaining essentially unchanged. It was popularised in the</p>
      <p class="letter__para">Lorem Ipsum is simply dummy text of the printing and typesetting industry. Lorem Ipsum has been the industry's standard dummy text ever since the 1500s, when an unknown printer took a galley of type and scrambled it to make a type specimen book. It has survived not only five centuries, but also the leap into electronic typesetting, remaining essentially unchanged. It was popularised in the</p>
      <div class="letter__signature" role="img" aria-label="Handwritten signature of the sender"></div>
    </section>

    <footer class="footer-band">
      <span class="footer-band__mark"></span>
      <div class="footer-band__panel">
        <p class="footer-band__name">Northvale Petrotek FZCO,</p>
        <p class="footer-band__line">Unit No. 2378, FZCO Trade Hub, level No. 1, K&amp;P 7, Dubai, United Arab Emirates</p>
        <p class="footer-band__line">Northvale Petrotek FZCO is registered as a free zone company under the rules &amp; regulations of FZCO</p>
      </div>
    </footer>
  </main>
</body>
</html>
```